Alcohol Marketing website

Home page and information page design, details as follows

CLIENT PURPOSE
Increase online visibility and create good contacts to increase business.

SERVICES
Drinks Marketing Consultancy
Brand Representation
Spirit Brand Sales & Marketing
Brand Development
Brand Distribution
Brand Launch & Introductions

COMPETITION
hazelpour.co.uk -
quintaloft.co.uk -

WEBSITE(S) CLIENT LIKES
Small competitors I admire:
http://www.hazelpour.co.uk/main.htm
http://www.quintaloft.com
http://www.morvatide.co.uk/spiritsliqueursbybrand.php
http://www.kelbrowhouse.com/page1.html
http://www.quorrifenwave.co.uk/index.asp

Nice page layout:
http://www.nkplume.com/
http://www.wzoharbour.com/
http://www.pelvit.com/index.cfm?do=pelvit.home

WEBSITE CLIENT DOES NOT LIKE
http://www.corvanhall.com/
http://www.amberlode-hall.com/
http://www.thesupperfold.co.uk/aboutUs.html
http://www.grainandkettle.com/
http://www.tessmarrow.co.uk/default.asp
http://www.pinnock-halden.co.uk/start.htm
http://www.rilby.co.uk/
http://www.vmkettles.com/default2.aspx
http://www.tumbril-vale.co.uk/mainpage.aspx

COMPANY LOGO
Customer has a company logo (Supplied)

COLOURS:
Blue
White

STRAPLINE:
No

WEBSITE THEME: Marketing

IMAGES THAT BEST REFLECT THE COMPANY:
Spirits / Drinks

HEADER IMAGE:
Spirits / Brands

PAGES:
home
keel& cask
a little about us
our spirit marketing
big brand success
speak to us

USER JOURNEYS:
General Service > Land on website >Navigation > Info Pages > Contact Form
Questions > Land on website > Message Banners > Info Pages > Contact Form
Contact > Land on website > Clear Telephone / Email Banner > Contact Form

CALL TO ACTION BANNER:
If you need help making your drink the next big brand, speak to us today.

KEYWORDS THAT RELATE TO THE BUSINESS:
brand marketing
drinks marketing
spirits marketing
brand marketing strategy
alcoholic drinks marketing
Drinks Brand Development

LOCATION(S):
United Kingdom -
Worldwide -

Target Market(s)

Male & Female
30-60
Marketing Directors
Brand Developers
Export Directors
Brand Managers

Industry/Entity Type

Marketing

Number of Pages Required

2 pages

Requirements
Must have
• This design will be integrated into wordpress, I have attached a wireframe of what we need, this is NOT a strict guide but contains content that is essential, the wireframes shows the priority of statements and products. the images supplied need to sell the products and services.
The main banner will eventually be animated so this needs to be taken into account.
The cliemt has supplied images which will need to be used in the design , however if you feel you have better images in the same style then they can be used.
Nice to have
• animation included, Jquery
Should not have
• NO fully flash sites or designs, this site will be Search engine optimised and updateable

```html
<!DOCTYPE html>
<html lang="en">
<head>
<meta charset="utf-8">
<title>Keel &amp; Cask – drinks brand marketing</title>
<link href="https://fonts.googleapis.com/css2?family=Roboto:wght@300;400&family=Open+Sans:ital,wght@0,400;0,700;1,400&display=swap" rel="stylesheet">
<style>
  :root{
    --ink:#0b111d;
    --bar:#151b29;
    --bar-line:#2b3345;
    --sky:#3ab4ea;
    --divider:#1ba3df;
    --lead:#4aa8e8;
    --body:#8d9bb3;
    --white:#ffffff;
    --grey:#b9c2d0;
    --red:#e3262c;
  }
  *{box-sizing:border-box;margin:0;padding:0}
  html,body{width:680px;height:1200px;overflow:hidden;background:var(--ink)}
  body{position:relative;font-family:"Open Sans",Arial,sans-serif;color:var(--white)}

  .page{position:absolute;left:0;width:680px;height:595px;overflow:hidden;
    background:linear-gradient(180deg,#0c1220 0%,#0a0f1a 100%)}
  .page--home{top:0}
  .page--about{top:605px}
  .divider{position:absolute;left:0;top:595px;width:680px;height:10px;background:var(--divider)}

  .topbar{position:absolute;left:0;top:0;width:680px;height:33px;background:var(--bar);
    border-bottom:1px solid var(--bar-line);display:flex;align-items:center;justify-content:space-between;padding:0 38px 0 25px;font-size:8px;color:var(--grey)}
  .social{display:flex;align-items:center;gap:6px}
  .social__name{font-weight:700;font-size:10px;color:var(--white)}
  .utility a{color:var(--grey);text-decoration:none}
  .utility span{color:#555e70;margin:0 4px}

  .hero{position:absolute;left:0;top:33px;width:680px;height:217px}
  .hero__photo{position:absolute;inset:0}
  .hero__photo--bar{background:
      linear-gradient(180deg,rgba(10,14,26,.35) 0%,rgba(0,0,0,0) 30%,rgba(0,0,0,0) 60%,rgba(28,70,140,.75) 100%),
      linear-gradient(100deg,#2a1c2a 0%,#4e2e34 14%,#6a4a4c 26%,#8a7a86 38%,#c9c8d0 47%,#e6e4ea 53%,#9a8a80 60%,#c47a2a 66%,#7a5a3a 72%,#3a2e30 84%,#1e1c2a 100%)}
  .hero__photo--glass{background:
      linear-gradient(180deg,rgba(20,16,14,.3) 0%,rgba(0,0,0,0) 25%,rgba(0,0,0,0) 62%,rgba(190,180,170,.35) 82%,rgba(30,60,110,.75) 100%),
      linear-gradient(90deg,#231a16 0%,#3c2a1c 12%,#7a4a1e 24%,#c07424 36%,#e0a04a 46%,#d08a30 54%,#9a5a1e 66%,#4a3222 80%,#2c2428 100%)}
  .hero__pitch{position:absolute;left:25px;top:35px;font-family:"Roboto",Arial,sans-serif;font-weight:300;color:var(--white);line-height:1;text-shadow:0 1px 3px rgba(0,0,0,.5)}
  .hero__pitch .line{display:block;font-size:19.5px}
  .hero__pitch .line--indent{padding-left:30px}
  .hero__pitch .big{display:block;font-size:48px;letter-spacing:-1px;margin:1px 0 -2px}
  .hero__pitch .line--tail{padding-left:36px}
  .hero__cta{position:absolute;left:84px;top:141px;width:102px;height:24px;border-radius:12px;
    background:linear-gradient(180deg,#f4f4f4,#b9bcc2);color:#4a4f59;font-family:"Roboto",Arial,sans-serif;
    font-weight:300;font-size:14px;text-align:center;line-height:24px;box-shadow:0 1px 3px rgba(0,0,0,.6)}

  .brand-card{position:absolute;right:0;top:37px;width:132px;height:94px;background:var(--white);
    display:flex;flex-direction:column;align-items:center;justify-content:center;gap:8px}
  .brand-card__name{font-family:"Roboto",Arial,sans-serif;font-weight:400;font-size:12px;color:#1d2330;letter-spacing:.5px}
  .brand-card__dot{width:16px;height:16px;border-radius:50%;background:var(--sky)}
  .contact-card{position:absolute;right:0;top:133px;width:132px;height:35px;background:var(--white);padding:3px 0 0 7px}
  .contact-card__phone{font-family:"Roboto",Arial,sans-serif;font-weight:300;font-size:15px;color:var(--sky);line-height:16px}
  .contact-card__mail{font-size:6.5px;color:var(--sky)}

  .nav{position:absolute;left:0;top:250px;width:680px;height:45px;
    background:radial-gradient(ellipse 360px 45px at 340px 0,rgba(40,110,190,.55),rgba(0,0,0,0) 80%),linear-gradient(180deg,#102544,#0c1424);
    display:flex;padding:0 0 0 3px}
  .nav__item{flex:0 0 auto;height:45px;display:flex;align-items:center;justify-content:center;
    font-family:"Roboto",Arial,sans-serif;font-weight:300;font-size:13.5px;color:#9aa8bd;border-right:1px solid rgba(80,110,150,.35);white-space:nowrap}
  .nav__item:last-child{border-right:none}
  .nav__item--active{color:var(--white)}
  .nav__item--active span{border-bottom:2px solid var(--red);padding:0 6px 2px}
  .w1{width:112px}.w2{width:113px}.w3{width:113px}.w4{width:113px}.w5{width:113px}.w6{width:110px}

  .content{position:absolute;left:25px;top:298px;width:630px}
  .content__title{font-family:"Roboto",Arial,sans-serif;font-weight:300;font-size:20.5px;color:var(--white);margin-bottom:6px}
  .content__lead{font-size:7.6px;font-weight:700;color:var(--lead);line-height:10px;margin-bottom:10px}
  .content__body{font-size:6.9px;color:var(--body);line-height:9.7px}
  .content--narrow{width:410px}
  .content__photo{position:absolute;left:468px;top:305px;width:195px;height:124px;
    background:
      linear-gradient(180deg,rgba(0,0,0,0) 50%,rgba(150,160,80,.45) 62%,rgba(0,0,0,0) 74%),
      linear-gradient(100deg,#3e6ea4 0%,#6a96c4 22%,#c8d8e8 42%,#eef2f6 52%,#b8cce0 64%,#7aa2cc 82%,#4a78aa 100%)}

  .cards{position:absolute;left:17px;top:432px;width:650px;height:114px}
  .page--about .cards{top:437px;left:19px}
  .card{position:absolute;top:0;width:209px;height:114px;border-radius:6px;
    background:linear-gradient(160deg,#1e4d85 0%,#12315a 55%,#0c1e38 100%);border:1px solid #24476f}
  .card:nth-child(1){left:0}.card:nth-child(2){left:219px}.card:nth-child(3){left:440px}
  .card__thumb{position:absolute;left:4px;top:6px;width:80px;height:74px;border:1px solid #fff}
  .thumb--bottles{background:
      linear-gradient(180deg,rgba(30,20,10,.6) 0%,rgba(0,0,0,0) 35%,rgba(0,0,0,0) 70%,rgba(200,140,40,.5) 100%),
      linear-gradient(90deg,#4a3020 0%,#c8b080 15%,#6a7a5a 30%,#e0d8c0 45%,#8a5a30 58%,#d0c8b0 72%,#5a6a4a 86%,#a07040 100%)}
  .thumb--cocktail{background:
      linear-gradient(180deg,#5a3a2a 0%,#c86a4a 30%,#e0a070 45%,#b8c880 62%,#d8e070 75%,#6a5a3a 100%)}
  .thumb--bubbles{background:
      linear-gradient(90deg,#5a6a78 0%,#a8b8c4 25%,#dfe6ec 45%,#b8c4cc 60%,#d07a30 75%,#a04818 88%,#4a2a18 100%)}
  .card__title{position:absolute;left:90px;top:12px;font-family:"Roboto",Arial,sans-serif;font-weight:300;font-size:16.5px;line-height:16px;color:var(--sky)}
  .card__text{position:absolute;left:4px;top:84px;width:200px;font-size:7.6px;font-weight:700;line-height:10px;color:var(--white)}
  .card__more{position:absolute;right:16px;bottom:0;font-size:7.6px;font-style:italic;color:var(--white)}

  .footer{position:absolute;left:0;top:556px;width:680px;text-align:center;font-size:6.8px;line-height:10px;color:var(--body)}
  .page--about .footer{top:561px}
</style>
</head>
<body>

<section class="page page--home">
  <header class="topbar">
    <div class="social">follow <span class="social__name">Chatterbox</span> <span class="social__name">Friendwall</span></div>
    <div class="utility"><a href="#">search</a><span>|</span><a href="#">sitemap</a></div>
  </header>
  <div class="hero">
    <div class="hero__photo hero__photo--bar" role="img" aria-label="Photograph of a row of cocktail glasses on a bar, garnished with physalis"></div>
    <h1 class="hero__pitch">
      <span class="line">If you need help making</span>
      <span class="line line--indent">your drink the next</span>
      <span class="big">big brand,</span>
      <span class="line line--tail">speak to us today.</span>
    </h1>
    <a class="hero__cta">read more</a>
    <div class="brand-card"><span class="brand-card__dot"></span><span class="brand-card__name">KEEL &amp; CASK</span></div>
    <div class="contact-card"><div class="contact-card__phone">t: 020 7946 0321</div><div class="contact-card__mail">e: info@keelandcask.com</div></div>
  </div>
  <nav class="nav">
    <div class="nav__item nav__item--active w1"><span>home</span></div>
    <div class="nav__item w2">keel&amp; cask</div>
    <div class="nav__item w3">a little about us</div>
    <div class="nav__item w4">our spirit marketin</div>
    <div class="nav__item w5">big brand success</div>
    <div class="nav__item w6">speak to us</div>
  </nav>
  <main class="content">
    <h2 class="content__title">Welcome</h2>
    <p class="content__lead">Lorem ipsum dolor sit amet, consec tetuer adipi scing elit. Praesent vestibulum molestie lacus. Aenean nonummy hendrerit mauris.</p>
    <p class="content__body">Phasellus porta. Fusce suscipit varius mi. Cum sociis natoque penatibus et magnis dis parturient montes, nascetur ridiculus mus. Nulla dui. Fusce feugiat malesuada odio. Morbi nunc odio, gravida at, cursus nec, luctus a, lorem. Maecenas tristique orci ac sem. Duis ultricies pharetra magna. Donec accumsan malesuada orci.<br>Donec sit amet eros.<br>&nbsp;Lorem ipsum dolor sit amet, consectetuer adipiscing elit. Mauris fermentum dictum magna. Sed laoreet aliquam leo. Ut tellus dolor, dapibus eget, elementum vel, cursus eleifend, elit. Aenean auctor wisi et urna. Aliquam erat volutpat. Duis ac turpis. Integer rutrum ante eu lacus</p>
  </main>
  <div class="cards">
    <article class="card"><div class="card__thumb thumb--bottles" role="img" aria-label="Photograph of spirit bottles on a back bar"></div><h3 class="card__title">22 years<br>experience<br>with big brands</h3><p class="card__text">Lorem ipsum dolor sit amet, consec tetuer adipi scing elit. Aenean nonummy hendrerit mauris.</p><span class="card__more">LEARN MORE</span></article>
    <article class="card"><div class="card__thumb thumb--cocktail" role="img" aria-label="Photograph of colourful cocktails"></div><h3 class="card__title">Making your<br>drink the next<br>big brand</h3><p class="card__text">Lorem ipsum dolor sit amet, consec tetuer adipi scing elit. Aenean nonummy hendrerit mauris.</p><span class="card__more">LEARN MORE</span></article>
    <article class="card"><div class="card__thumb thumb--bubbles" role="img" aria-label="Photograph of a sparkling drink with bubbles"></div><h3 class="card__title">350 outlets that<br>listen to what<br>we say</h3><p class="card__text">Lorem ipsum dolor sit amet, consec tetuer adipi scing elit. Aenean nonummy hendrerit mauris.</p><span class="card__more">LEARN MORE</span></article>
  </div>
  <footer class="footer">brand marketing | brand marketing strategy | drinks marketing | spirits marketing | alcoholic drinks marketing | drinks brand development<br>© 1999-2010 Keel &amp; Cask | terms and conditions | privacy policy</footer>
</section>

<div class="divider"></div>

<section class="page page--about">
  <header class="topbar">
    <div class="social">follow <span class="social__name">Chatterbox</span> <span class="social__name">Friendwall</span></div>
    <div class="utility"><a href="#">search</a><span>|</span><a href="#">sitemap</a></div>
  </header>
  <div class="hero">
    <div class="hero__photo hero__photo--glass" role="img" aria-label="Close-up photograph of an amber cocktail in a martini glass"></div>
    <div class="brand-card"><span class="brand-card__dot"></span><span class="brand-card__name">KEEL &amp; CASK</span></div>
    <div class="contact-card"><div class="contact-card__phone">t: 020 7946 0321</div><div class="contact-card__mail">e: info@keelandcask.com</div></div>
  </div>
  <nav class="nav">
    <div class="nav__item w1">home</div>
    <div class="nav__item w2">keel&amp; cask</div>
    <div class="nav__item nav__item--active w3"><span>a little about us</span></div>
    <div class="nav__item w4">our spirit marketin</div>
    <div class="nav__item w5">big brand success</div>
    <div class="nav__item w6">speak to us</div>
  </nav>
  <main class="content content--narrow">
    <h2 class="content__title">a little bit about us</h2>
    <p class="content__lead">Lorem ipsum dolor sit amet, consec tetuer adipi scing elit. Praesent vestibulum molestie lacus. Aenean nonummy hendrerit mauris.</p>
    <p class="content__body">Phasellus porta. Fusce suscipit varius mi. Cum sociis natoque penatibus et magnis dis parturient montes, nascetur ridiculus mus. Nulla dui. Fusce feugiat malesuada odio. Morbi nunc odio, gravida at, cursus nec, luctus a, lorem. Maecenas tristique orci ac sem. Duis ultricies pharetra magna. Donec accumsan malesuada orci.<br>Donec sit amet eros.<br>&nbsp;Lorem ipsum dolor sit amet, consectetuer adipiscing elit. Mauris fermentum dictum magna. Sed laoreet aliquam leo. Ut tellus dolor, dapibus eget, elementum vel, cursus eleifend, elit. Aenean auctor wisi et urna. Aliquam erat volutpat. Duis ac turpis. Integer rutrum ante eu lacus</p>
  </main>
  <div class="content__photo" role="img" aria-label="Photograph of a martini with an olive"></div>
  <div class="cards">
    <article class="card"><div class="card__thumb thumb--bottles" role="img" aria-label="Photograph of spirit bottles on a back bar"></div><h3 class="card__title">22 years<br>experience<br>with big brands</h3><p class="card__text">Lorem ipsum dolor sit amet, consec tetuer adipi scing elit. Aenean nonummy hendrerit mauris.</p><span class="card__more">LEARN MORE</span></article>
    <article class="card"><div class="card__thumb thumb--cocktail" role="img" aria-label="Photograph of colourful cocktails"></div><h3 class="card__title">Making your<br>drink the next<br>big brand</h3><p class="card__text">Lorem ipsum dolor sit amet, consec tetuer adipi scing elit. Aenean nonummy hendrerit mauris.</p><span class="card__more">LEARN MORE</span></article>
    <article class="card"><div class="card__thumb thumb--bubbles" role="img" aria-label="Photograph of a sparkling drink with bubbles"></div><h3 class="card__title">350 outlets that<br>listen to what<br>we say</h3><p class="card__text">Lorem ipsum dolor sit amet, consec tetuer adipi scing elit. Aenean nonummy hendrerit mauris.</p><span class="card__more">LEARN MORE</span></article>
  </div>
  <footer class="footer">brand marketing | brand marketing strategy | drinks marketing | spirits marketing | alcoholic drinks marketing | drinks brand development<br>© 1999-2010 Keel &amp; Cask | terms and conditions | privacy policy</footer>
</section>

</body>
</html>
```